Travel Website Design

My client is a startup that will sell Ridgewater Hunts and fishing trips.
We do not have a logo as of yet, but I have attached 3 options for you to use in the mockup process. Please feel free to use any one (or all 3) of them, but don't base design around them.

Also attached is client's loose idea of how he wants an interior page to look. For the homepage, it would definitely need a rotating image slider, a search, and a tabbed section. The crestpinesafaris.com is probably closest to what he is looking for.

Here are a few websites to pass along. In addition to the logos I have attached some links of company websites that are competition and have similar designs and layouts similar to what I am looking for.

http://www.crestpinesafaris.com - The most direct competition that I have. I really like how they layout the pages and lodges info.

Varno.com - Close competition. Not a huge fan of how they search for lodges but like how they display each lodge and provide info.

http://www.qrandel.com/ - Example of a company website and layout the client does not like.

http://stonemeadjourneys.com/ - Clean feel. Not a fan of how they layout each lodges info.

```html
<!DOCTYPE html>
<html lang="en">
<head>
<meta charset="utf-8">
<title>Ridgewater Hunts – Home</title>
<link href="https://fonts.googleapis.com/css2?family=Ubuntu:ital,wght@0,400;0,500;0,700;1,400&display=swap" rel="stylesheet">
<style>
:root{
  --blue:#0a6f99;
  --blue-dark:#07577a;
  --ink:#1d1d1d;
  --text:#3a3a3a;
  --panel:#efeff4;
  --page:#e4e4ea;
  --white:#ffffff;
  --footer:#1c1c1c;
}
*{box-sizing:border-box;margin:0;padding:0}
html,body{width:1073px;height:1200px;overflow:hidden}
body{position:relative;background:var(--page);font-family:'Ubuntu',sans-serif;color:var(--text)}
.abs{position:absolute}

.site-header{left:0;top:0;width:1073px;height:110px;background:var(--white);border-top:3px solid var(--ink)}
.brand{left:124px;top:30px;display:flex;align-items:center;gap:10px}
.brand-mark{width:44px;height:44px;border-radius:50%;background:var(--blue)}
.brand-name{font-size:30px;font-weight:700;color:var(--ink);line-height:1}
.member-tab{left:611px;top:0;width:158px;height:32px;background:var(--ink);color:#fff;font-size:14px;font-weight:500;display:flex;align-items:center;justify-content:center;border-radius:0 0 4px 4px}
.social-tab{left:790px;top:0;width:157px;height:32px;background:var(--ink);border-radius:0 0 4px 4px;display:flex;align-items:center;justify-content:center;gap:11px}
.social-tab span,.footer-social span{width:23px;height:23px;border-radius:4px;background:var(--blue)}
.quote-line{right:124px;top:75px;font-size:20px;color:var(--blue);font-weight:500;display:flex;align-items:center;gap:6px;white-space:nowrap}
.quote-line b{color:var(--ink);font-weight:500}
.quote-line .phone{color:var(--ink);margin-left:4px}

.header-rule{left:0;top:110px;width:1073px;height:5px;background:var(--ink)}
.main-nav{left:0;top:115px;width:1073px;height:39px;background:linear-gradient(#1082b2,var(--blue-dark))}
.main-nav a{position:absolute;top:0;height:39px;line-height:39px;color:#dceef6;text-decoration:none;font-size:13px;font-weight:500;text-align:center}
.main-nav a.active{background:#111;color:#fff}
.nav-sep{position:absolute;top:0;width:1px;height:39px;background:rgba(255,255,255,.25)}

.hero{left:0;top:154px;width:1073px;height:401px;background:linear-gradient(180deg,#3b5e8a 0%,#2c4d78 35%,#8a6a55 70%,#b99a84 100%)}
.slider-bar{left:130px;top:480px;width:812px;height:30px;background:rgba(20,20,20,.88);display:flex;align-items:center}
.slider-bar .ask{width:316px;padding-left:19px;color:#fff;font-size:18px}
.slider-bar .choose{width:231px;height:30px;background:var(--blue);color:#fff;font-size:18px;display:flex;align-items:center;justify-content:center;gap:8px}
.dots{position:absolute;left:721px;top:10px;display:flex;gap:7px}
.dots i{width:10px;height:10px;border-radius:50%;background:#fff}
.dots i.on{background:var(--blue)}

.content-panel{left:130px;top:519px;width:812px;height:551px;background:var(--panel);border-radius:3px}
.welcome{left:149px;top:545px;display:flex;align-items:center;gap:8px;font-size:20px;color:var(--blue)}
.welcome .dot{width:22px;height:22px;border-radius:50%;background:var(--blue)}
.welcome strong{color:var(--ink);font-weight:700}
.dotted-rule{left:149px;top:578px;width:561px;border-top:1px dotted #888}
.intro{left:149px;top:586px;width:563px;font-size:11.4px;line-height:18.6px;color:var(--text)}
.intro p+p{margin-top:9px}

.testimonials-tab{left:743px;top:527px;width:174px;height:28px;background:var(--blue);color:#fff;font-size:15px;font-weight:500;display:flex;align-items:center;justify-content:center}
.testimonial-box{left:737px;top:555px;width:186px;height:202px;background:#f5f5f8;border:1px solid #d6d6dc;border-radius:4px;padding:14px 12px 0 14px}
.testimonial-box blockquote{font-style:italic;font-size:11.6px;line-height:18.6px;color:#444;letter-spacing:.3px}
.testimonial-box blockquote::before{content:"\201C";font-size:40px;color:#bbb;line-height:0;vertical-align:-14px;margin-right:4px}
.testimonial-box blockquote::after{content:"\201D";font-size:40px;color:#bbb;line-height:0;vertical-align:-18px;margin-left:4px}
.testimonial-box cite{display:block;margin-top:14px;font-style:normal;font-weight:500;font-size:12.5px;color:var(--ink)}
.view-all{display:inline-block;margin-top:12px;background:var(--blue);color:#fff;font-size:12px;padding:3px 9px;border-radius:2px}

.feature{position:absolute;top:782px;width:186px}
.feature h2{font-size:19px;font-weight:500;color:#333;margin-left:4px;white-space:nowrap}
.feature h2 span{color:var(--blue)}
.feature .frame{margin-top:7px;width:186px;height:108px;background:#fff;border:1px solid #d0d0d6;padding:4px;box-shadow:0 6px 6px -5px rgba(0,0,0,.35)}
.feature .photo{width:100%;height:100%}
.feature p{margin:25px 0 0 5px;font-size:11.8px;line-height:14px;color:#444;letter-spacing:.5px}
.read-more{position:absolute;right:4px;top:210px;display:flex;height:18px;font-size:11px;color:#fff}
.read-more .label{background:var(--blue);padding:0 8px;line-height:18px;border-radius:2px 0 0 2px}
.read-more .go{width:19px;background:#222;display:flex;align-items:center;justify-content:center;border-radius:0 2px 2px 0}

.site-footer{left:0;top:1049px;width:1073px;height:151px;background:var(--footer);border-bottom:3px solid var(--blue)}
.footer-nav{left:0;top:1090px;width:1073px;text-align:center;color:#fff;font-size:12px;font-weight:500}
.footer-nav span{margin:0 6px;color:#bbb}
.footer-social{left:0;top:1124px;width:1073px;display:flex;justify-content:center;gap:13px}
.copyright{left:0;top:1166px;width:1073px;text-align:center;color:#fff;font-size:12px}
</style>
</head>
<body>

<header class="abs site-header">
  <div class="abs brand"><span class="brand-mark"></span><span class="brand-name">Ridgewater Hunts</span></div>
</header>
<div class="abs member-tab">Become A Member</div>
<div class="abs social-tab" aria-label="Social links"><span></span><span></span><span></span><span></span></div>
<div class="abs quote-line">Request a <b>FREE</b> Quote
  <svg width="18" height="20" viewBox="0 0 18 20"><path d="M4 2l3 4-2 2c1 3 3 5 6 6l2-2 4 3-2 3C8 17 2 11 2 4z" fill="#1d1d1d"/></svg>
  Call: <span class="phone">1.555.014.7720</span></div>

<div class="abs header-rule"></div>
<nav class="abs main-nav">
  <a class="active" style="left:125px;width:108px">Home</a>
  <a style="left:233px;width:153px">About Us</a>
  <span class="nav-sep" style="left:386px"></span>
  <a style="left:386px;width:182px">Conversation</a>
  <span class="nav-sep" style="left:568px"></span>
  <a style="left:568px;width:127px">Blog</a>
  <span class="nav-sep" style="left:695px"></span>
  <a style="left:695px;width:138px">Travel</a>
  <span class="nav-sep" style="left:833px"></span>
  <a style="left:833px;width:166px">Contact Us</a>
</nav>

<div class="abs hero" role="img" aria-label="Slider photo: four anglers on a boat holding up their fish against the sea"></div>
<div class="abs slider-bar">
  <div class="ask">WHERE DO YOU WANT TO FISH?</div>
  <div class="choose">CHOOSE DESTINATION
    <svg width="14" height="10" viewBox="0 0 14 10"><path d="M2 8l5-5 5 5" stroke="#fff" stroke-width="3" fill="none"/></svg></div>
  <div class="dots"><i></i><i class="on"></i><i></i><i></i><i></i></div>
</div>

<main class="abs content-panel"></main>
<h1 class="abs welcome" style="font-weight:400"><span class="dot"></span>Welcome to <strong>Ridgewater Hunts</strong></h1>
<div class="abs dotted-rule"></div>
<div class="abs intro">
  <p>Lorem ipsum dolor sit amet, consectetuer adipiscing elit, sed diam nonummy nibh euismod tincidunt ut laoreet dolore magna aliquam erat volutpat. Ut wisi enim ad minim veniam, quis nostrud exerci tation ullamcorper suscipit lobortis nisl ut aliquip ex ea commodo consequat. Duis autem vel eum iriure dolor in hendrerit in vulputate velit esse molestie consequat.</p>
  <p>Lorem ipsum dolor sit amet, consectetuer adipiscing elit, sed diam nonummy nibh euismod tincidunt ut laoreet dolore magna aliquam erat volutpat. Ut wisi enim ad minim veniam, quis nostrud exerci tation ullamcorper suscipit lobortis nisl ut aliquip ex ea commodo consequat. Duis autem vel eum iriure dolor in hendrerit in vulputate velit esse molestie consequat.</p>
</div>

<div class="abs testimonials-tab">Testimonials</div>
<aside class="abs testimonial-box">
  <blockquote>Lorem ipsum dolor sit amet consetug e sed diay nibh euismodl tincidunt ut laoreet dolore magam er vol wisi enim ad minim veniam quis nostrud exerci</blockquote>
  <cite>Mr.Callum Ferris</cite>
  <span class="view-all">View All</span>
</aside>

<section class="feature" style="left:148px">
  <h2>Travel <span>Blog</span></h2>
  <div class="frame"><div class="photo" role="img" aria-label="Two anglers wading a river with fly rods" style="background:linear-gradient(#3f6a35,#56703f 55%,#8e9683)"></div></div>
  <p>Lorem ipsum dolor sit amet consectetuer adipiscing elit, sed diam nonummy nibh</p>
  <div class="read-more"><span class="label">Read More</span><span class="go"><svg width="9" height="9"><path d="M1 1l4 3.5L1 8M4 1l4 3.5L4 8" stroke="#fff" fill="none"/></svg></span></div>
</section>
<section class="feature" style="left:345px">
  <h2>Specials <span>&amp; Deals</span></h2>
  <div class="frame"><div class="photo" role="img" aria-label="Angler beside a raft on a lake lined with pines" style="background:linear-gradient(#2f86d6,#3c6d4a 45%,#2f7fa8)"></div></div>
  <p>Lorem ipsum dolor sit amet consectetuer adipiscing elit, sed diam nonummy nibh</p>
  <div class="read-more"><span class="label">Read More</span><span class="go"><svg width="9" height="9"><path d="M1 1l4 3.5L1 8M4 1l4 3.5L4 8" stroke="#fff" fill="none"/></svg></span></div>
</section>
<section class="feature" style="left:542px">
  <h2>Hosted <span>&amp; Trips</span></h2>
  <div class="frame"><div class="photo" role="img" aria-label="Anglers casting from a boat on open sea" style="background:linear-gradient(#7db7e2,#2f74b0 50%,#1f5f95)"></div></div>
  <p>Lorem ipsum dolor sit amet consectetuer adipiscing elit, sed diam nonummy nibh</p>
  <div class="read-more"><span class="label">Read More</span><span class="go"><svg width="9" height="9"><path d="M1 1l4 3.5L1 8M4 1l4 3.5L4 8" stroke="#fff" fill="none"/></svg></span></div>
</section>
<section class="feature" style="left:739px">
  <h2>Couples<span>/Family</span></h2>
  <div class="frame"><div class="photo" role="img" aria-label="Couple on a boat holding two large fish" style="background:linear-gradient(#5e9ad4,#5f8a5c 55%,#c9c9c4)"></div></div>
  <p>Lorem ipsum dolor sit amet consectetuer adipiscing elit, sed diam nonummy nibh</p>
  <div class="read-more"><span class="label">Read More</span><span class="go"><svg width="9" height="9"><path d="M1 1l4 3.5L1 8M4 1l4 3.5L4 8" stroke="#fff" fill="none"/></svg></span></div>
</section>

<footer class="abs site-footer" style="z-index:-1"></footer>
<div class="abs footer-nav">Home<span>|</span>About Us<span>|</span>Conversation<span>|</span>Blog<span>|</span>Travel<span>|</span>Contact Us</div>
<div class="abs footer-social" aria-label="Social links"><span></span><span></span><span></span><span></span></div>
<div class="abs copyright">© 2014 Ridgewater Hunts All Rights Reserved.</div>

</body>
</html>
```